Holiday Villa in the Sri Lankan hills requires a promotional flyer

We are a holiday villa set in the hills of Sri Lanka. We are aiming to encourage travellers visiting the nearby city of Kandy for the Kandy festival to stay at our villa which is more peaceful than the crowded city. The festival is a colourful one with lots of elephants, fire dancers etc. while our villa is set in a peaceful village which is surrounded by trees and water. The design should communicate the escape to nature and quiet. The flyer is aimed at travel agents and will be sent to them as an e-flyer. It needs to be a one pager which can be sent by email. The aim is to increase our bookings over the period of July and August.
Travel agents
Travel Industry

```html
<!DOCTYPE html>
<html lang="en">
<head>
<meta charset="utf-8">
<title>The Ferncliff House – Perahera Flyer</title>
<link href="https://fonts.googleapis.com/css2?family=Raleway:ital,wght@0,300;0,400;0,500;0,700;0,800;1,700&display=swap" rel="stylesheet">
<style>
  :root {
    --bg: #8c8c8c;
    --teal: #0b7381;
    --cyan: #12a8c3;
    --cyan-light: #5ccbdc;
    --white: #ffffff;
    --night: #1b1f5c;
    --gold: #e7b45a;
  }
  * { margin: 0; padding: 0; box-sizing: border-box; }
  html, body { width: 1200px; height: 1200px; overflow: hidden; }
  body {
    background: var(--bg);
    font-family: "Raleway", sans-serif;
    color: var(--white);
  }
  .flyer {
    position: absolute;
    left: 200px; top: 34px;
    width: 800px; height: 1132px;
    background: var(--teal);
    overflow: hidden;
  }
  .hero-photo {
    position: absolute; left: 0; top: 0; width: 800px; height: 430px;
    background: linear-gradient(180deg, var(--night) 0%, #2c2a55 30%, #8a6a3c 55%, var(--gold) 80%, #c99a45 100%);
  }
  .waves { position: absolute; inset: 0; width: 800px; height: 1132px; }
  .headline {
    position: absolute; left: 48px; top: 440px;
    font-size: 42px; line-height: 48px; font-weight: 300;
    letter-spacing: -1px; text-transform: uppercase;
  }
  .headline strong { font-weight: 800; }
  .escape {
    position: absolute; left: 48px; top: 554px;
    font-size: 32px; font-weight: 800; color: var(--cyan-light);
    letter-spacing: -0.8px; text-transform: uppercase;
  }
  .tagline {
    position: absolute; left: 48px; top: 595px;
    font-size: 17px; font-weight: 700; font-style: italic;
  }
  .perks-title {
    position: absolute; left: 48px; top: 645px;
    font-size: 21px; font-weight: 700; letter-spacing: -0.4px;
  }
  .perks {
    position: absolute; left: 48px; top: 676px; width: 400px;
    list-style: none; font-size: 20px; font-weight: 400; line-height: 25px;
  }
  .perks li { position: relative; padding-left: 28px; margin-bottom: 8px; }
  .perks li::before { content: "•"; position: absolute; left: 0; font-size: 14px; }
  .room-photo {
    position: absolute; left: 455px; top: 633px;
    width: 300px; height: 300px; border-radius: 50%;
    border: 12px solid var(--white);
    background: radial-gradient(circle at 50% 35%, #f3eee6 0%, #cdb79a 45%, #7a4a33 75%, #4a2a1f 100%);
    box-shadow: 0 14px 24px rgba(0,0,0,0.25);
  }
  .brand-name {
    position: absolute; left: 48px; top: 1040px;
    font-size: 21px; font-weight: 400; color: var(--cyan);
    letter-spacing: 1px; text-transform: uppercase; white-space: nowrap;
  }
  .contact {
    position: absolute; right: 34px; top: 976px;
    list-style: none; text-align: right; font-size: 19px; line-height: 31px;
  }
  .contact li { display: flex; justify-content: flex-end; align-items: center; gap: 6px; }
  .contact .name { font-weight: 700; }
  .contact .address { padding-right: 26px; }
  .contact svg { width: 20px; height: 20px; }
</style>
</head>
<body>
  <main class="flyer">
    <div class="hero-photo" role="img" aria-label="Night view of the illuminated Temple of the Tooth in Kandy"></div>

    <svg class="waves" viewBox="0 0 800 1132" aria-hidden="true">
      <path d="M0,318 C110,395 220,415 320,410 C480,400 620,300 800,292 L800,1132 L0,1132Z" fill="var(--cyan)"/>
      <path d="M0,345 C110,405 220,420 320,413 C490,400 620,330 800,318 L800,1132 L0,1132Z" fill="var(--teal)"/>
      <path d="M0,868 C90,848 170,862 250,885 C380,918 480,908 580,875 C680,840 760,790 800,748 L800,1132 L0,1132Z" fill="var(--cyan)"/>
      <path d="M0,905 C90,880 170,892 260,908 C380,930 480,915 580,882 C680,848 760,800 800,770 L800,1132 L0,1132Z" fill="var(--white)"/>
      <path d="M305,1132 C385,975 525,925 800,885 L800,1132Z" fill="var(--cyan)"/>
      <path d="M330,1132 C400,990 540,950 800,930 L800,1132Z" fill="var(--teal)"/>
    </svg>

    <h1 class="headline">Experience the <strong>Kandy Perahera</strong><br>but <strong>getaway from the crowd</strong></h1>
    <h2 class="escape">Escape to The Ferncliff House</h2>
    <p class="tagline">Surround yourself in nature at a private villa just 45 minutes from Kandy</p>

    <h3 class="perks-title">WHEN YOU STAY WITH US YOU ENJOY</h3>
    <ul class="perks">
      <li>A pre-Perahera explanation on the significance of the festival</li>
      <li>A snack pack from our kitchens to munch on at the Perahera</li>
      <li>An activity kit for young kids to keep them entertained</li>
    </ul>

    <div class="room-photo" role="img" aria-label="Villa living room with sofas, lamps and a patterned rug"></div>

    <p class="brand-name">The Ferncliff House</p>

    <ul class="contact">
      <li><span class="name">The Ferncliff House</span>
        <svg viewBox="0 0 20 20"><circle cx="10" cy="10" r="8.5" fill="none" stroke="var(--white)" stroke-width="1.3"/><path d="M5.5,10 L10,6 L14.5,10 M7,9.5 V14 H13 V9.5" fill="none" stroke="var(--white)" stroke-width="1.4"/></svg></li>
      <li class="address">Meadowvale, Kandy District</li>
      <li>www.ferncliff-house.com
        <svg viewBox="0 0 20 20"><circle cx="10" cy="10" r="8.5" fill="none" stroke="var(--white)" stroke-width="1.3"/><circle cx="10" cy="10" r="4.5" fill="none" stroke="var(--white)" stroke-width="1.2"/><path d="M5.5,10 H14.5 M10,5.5 V14.5" stroke="var(--white)" stroke-width="1"/></svg></li>
      <li>information@ferncliff-house.com
        <svg viewBox="0 0 20 20"><circle cx="10" cy="10" r="8.5" fill="none" stroke="var(--white)" stroke-width="1.3"/><rect x="5.5" y="7" width="9" height="6.5" fill="none" stroke="var(--white)" stroke-width="1.2"/><path d="M5.5,7 L10,11 L14.5,7" fill="none" stroke="var(--white)" stroke-width="1.2"/></svg></li>
    </ul>
  </main>
</body>
</html>
```